Commercial Rooftop Solar business needs a website

We need a website with fantastic appeal for a new company based in Melbourne called Brightvale Energy. We design and install solar energy systems for commercial applications across Australia. Our market is to focus on small to medium businesses looking for solar solutions, but we will also provide our service for residential customers. We would like a beautiful 'front page' feel to our home page, using photographs of solar PV systems and/or natural imagery. Our logo uses the colours orange and black, which could easily be echoed in photographic imagery of sunset and sunrise, for example. The design should communicate quiet confidence and professionalism to a corporate marketplace.

NEW POINTS FOR BRIEF: This design also needs to be flexible to allow for additional future content, including a Support page with sub pages, FAQ's, and a Blog.

As part of this design project, we will require the coding for the website to be completed by the designer.

We have seen some websites, which we like the look and feel of: these are listed below.

keenroofpower.com.au:

• Beautiful images underlaying brief text selling points.
• Simple ‘front cover’ style home page with elegant drop-down menu, stylish simple font style.
• Home page invites exploration through the menu links, rather than trying to provide all the information up front.
• Company logo and name in the top left hand corner, contact details accessible at top right hand, seems consistent in most sites.

tolvaenergy.com.au

brinkeltpower.com:
• Same element as the others is the front-page style home page with beautiful images underlying text.

We have a webpage that we started uploading content to. You can use some of the content there in your designs: www.brightvaleenergy.com.au

Technical Specifications:
PAGES:

Home

About Us

Solutions - Commercial
- Residential

Products - Solar Panels - Morvo Falcon, Morvo CELT, Morvo KT
- Solar Inverters - Valtrex, SunPivot
- Monitoring systems - Lumen Metrics
- Batteries - QD

- Datasheets have been provided for reference but if it's too much work, you can use generic text and we will provide content later.

Contact Us

FUTURE PAGES (Please consider in structure, where links could be placed):

Support

FAQ's

Blog.

We could provide some content for the Support page soon, but the Blog and FAQ's are future pages which we don't want highlighted in the design as we don't yet have content.

Phone: 1800 7 VOLTA
Email: sales@brightvaleenergy.com.au

Currently, I do not have images and text available. Please
use placeholders in the meantime. The final text and images will be uploaded for the winner once a winning design has been selected.

Target Market(s)

Primary focus is on small to medium sized business owners. Those owners will have a house which may be suitable for solar so we want to cater to residential deeper in the website.

Industry/Entity Type

Solar Energy

Coding

Coded - Design and coding required

Number of Pages Required

5+ page

Colors
f78f20
0255a3

Requirements
Must have
• Logo as per attachments.
Nice to have
• Logo can have alternate colours Eg. White on Orange or Black etc. provided colour correct logo is shown somewhere eg. footer or contact page.
• In the active site, I'd like to have:
• Very slowly zooming images - barely perceptible.
• Title text that rolls into place
• Subtle movements
• See https://paylarkfinance.com.au/ for example

```html
<!DOCTYPE html>
<html lang="en">
<head>
<meta charset="utf-8">
<title>Brightvale Energy</title>
<link href="https://fonts.googleapis.com/css2?family=Montserrat:wght@400;500;600;700&family=Roboto:ital,wght@0,400;0,500;1,400&display=swap" rel="stylesheet">
<style>
:root{
  --orange:#f05a22;
  --orange-soft:#f47a3c;
  --ink:#222222;
  --text:#555555;
  --muted:#8a8a8a;
  --line:#e2e2e2;
  --panel:#f4f4f4;
  --white:#ffffff;
  --night:#1d2a3a;
}
*{box-sizing:border-box;margin:0;padding:0}
html,body{width:1200px;height:2899px;overflow:hidden}
body{position:relative;background:var(--white);font-family:'Roboto',sans-serif;color:var(--text)}
.accent{color:var(--orange)}
.btn{position:absolute;display:flex;align-items:center;justify-content:center;border-radius:20px;font-family:'Montserrat',sans-serif;font-size:14px;text-transform:uppercase;text-decoration:none;color:var(--white);background:var(--orange);white-space:nowrap}

/* Header */
.site-header{position:absolute;left:0;top:0;width:1200px;height:66px;background:var(--white);z-index:5}
.brand{position:absolute;left:100px;top:16px;display:flex;align-items:center;gap:10px;font-family:'Montserrat',sans-serif;font-weight:600;font-size:19px;color:var(--ink)}
.brand-dot{width:30px;height:30px;border-radius:50%;background:var(--orange)}
.main-nav{position:absolute;right:258px;top:25px;display:flex;gap:26px;font-family:'Montserrat',sans-serif;font-size:13px;color:var(--ink);text-transform:uppercase;white-space:nowrap}
.nav-contact{left:972px;top:16px;width:130px;height:35px;font-size:13px}

/* Hero */
.hero{position:absolute;left:0;top:66px;width:1200px;height:510px;clip-path:polygon(0 0,100% 0,100% 440px,0 100%)}
.hero-photo{position:absolute;inset:0;background:linear-gradient(120deg,#3c4a5c 0%,#5c6c7e 35%,#8a9099 55%,#4a5a6e 80%,#2f3d4e 100%)}
.hero-title{position:absolute;left:97px;top:153px;font-family:'Montserrat',sans-serif;font-weight:600;font-size:41px;line-height:52px;color:var(--white)}
.hero-btn{left:99px;top:282px;width:147px;height:40px;background:transparent;border:1.5px solid var(--white)}
.badge{position:absolute;width:70px;height:70px;border-radius:50%;background:var(--white);display:flex;align-items:center;justify-content:center;z-index:4}
.badge span{width:38px;height:38px;border-radius:50%;background:var(--orange)}
.badge-hero{left:565px;top:506px}

/* About */
.about-title{position:absolute;left:116px;top:614px;font-family:'Montserrat',sans-serif;font-size:35px;font-weight:400;color:var(--ink)}
.about-text{position:absolute;left:116px;top:670px;width:452px;font-size:13.5px;line-height:23px;color:var(--muted)}
.about-text p+p{margin-top:23px}
.about-btn{left:116px;top:867px;width:127px;height:34px}
.video{position:absolute;left:632px;top:620px;width:456px;height:276px;background:var(--white);box-shadow:0 0 8px rgba(0,0,0,.18);padding:4px}
.video-photo{width:100%;height:100%;background:linear-gradient(180deg,#3f86d6 0%,#76aee8 45%,#9aa6b4 60%,#2e3f5a 100%)}
.play{position:absolute;left:214px;top:104px;width:72px;height:72px}

/* Solutions */
.solutions{position:absolute;left:0;top:960px;width:1200px;height:489px;background:var(--panel)}
.section-title{position:absolute;left:0;width:1200px;text-align:center;font-family:'Montserrat',sans-serif;font-size:35px;font-weight:400;color:var(--ink)}
.section-lead{position:absolute;left:150px;width:900px;text-align:center;font-size:13px;line-height:24px;color:var(--muted)}
.solution-card{position:absolute;top:182px;width:300px;height:230px}
.solution-photo{position:absolute;left:0;top:0;width:300px;height:195px}
.solution-label{position:absolute;left:25px;top:160px;width:250px;height:70px;background:var(--white);text-align:center;padding-top:13px}
.solution-label h3{font-family:'Montserrat',sans-serif;font-weight:500;font-size:20px;color:var(--ink)}
.solution-label span{display:block;margin-top:5px;font-family:'Montserrat',sans-serif;font-size:11px;color:var(--orange);text-transform:uppercase}

/* Products */
.product-card{position:absolute;top:1629px;width:230px;height:278px;border:1px solid var(--line);background:var(--white)}
.product-photo{position:absolute;left:50px;top:55px;width:130px;height:170px;border-radius:4px}
.product-name{position:absolute;top:1928px;width:280px;text-align:center;font-family:'Montserrat',sans-serif;font-size:14px;line-height:21px;color:var(--ink);text-transform:uppercase}
.product-price{position:absolute;top:1980px;width:280px;text-align:center;font-family:'Montserrat',sans-serif;font-weight:500;font-size:19px;color:var(--orange)}
.all-btn{left:514px;top:2032px;width:171px;height:34px}

/* Testimonials */
.reviews{position:absolute;left:0;top:2106px;width:1200px;height:522px;clip-path:polygon(0 87px,100% 0,100% 100%,0 100%)}
.reviews-photo{position:absolute;inset:0;background:linear-gradient(180deg,#3a4658 0%,#5a5560 35%,#9a6a4a 55%,#4a4e5a 75%,#1f2a38 100%)}
.badge-reviews{left:564px;top:2100px}
.reviews-title{top:2200px;color:var(--white);font-weight:600;font-size:42px}
.avatar{position:absolute;border-radius:50%;border:3px solid var(--white)}
.review-text{position:absolute;left:210px;top:2386px;width:780px;text-align:center;font-size:15.5px;line-height:24px;color:var(--white)}
.review-name{position:absolute;left:0;top:2476px;width:1200px;text-align:center;font-family:'Montserrat',sans-serif;font-weight:500;font-size:19px;color:var(--white)}
.review-role{position:absolute;left:0;top:2503px;width:1200px;text-align:center;font-style:italic;font-size:15px;color:var(--white)}
.dots{position:absolute;left:575px;top:2541px;display:flex;gap:8px}
.dots i{width:9px;height:9px;border-radius:50%;background:var(--white)}
.dots i.on{background:var(--orange)}

/* Footer */
.site-footer{position:absolute;left:0;top:2628px;width:1200px;height:226px;background:var(--panel)}
.footer-brand{position:absolute;left:100px;top:92px;display:flex;align-items:center;gap:12px;font-family:'Montserrat',sans-serif;font-weight:600;font-size:22px;color:var(--orange)}
.footer-brand span{width:40px;height:40px;border-radius:50%;background:var(--orange)}
.footer-col{position:absolute;top:50px}
.footer-col h4{font-family:'Montserrat',sans-serif;font-weight:500;font-size:14px;color:var(--ink);text-transform:uppercase;letter-spacing:.5px;padding-bottom:10px;border-bottom:1px solid #cfcfcf;width:130px}
.footer-col ul{list-style:none;margin-top:12px}
.footer-col li{font-size:12.5px;line-height:22px;color:var(--text)}
.contact-list li{display:flex;align-items:flex-start;gap:12px;margin-bottom:4px}
.contact-list svg{flex:none;margin-top:4px}
.bottom-bar{position:absolute;left:0;top:2854px;width:1200px;height:45px;background:var(--orange)}
.copyright{position:absolute;left:99px;top:15px;font-size:12.5px;color:var(--white)}
.social{position:absolute;left:974px;top:9px;display:flex;gap:8px}
.social i{width:26px;height:26px;border-radius:50%;background:var(--white)}
</style>
</head>
<body>

<header class="site-header">
  <div class="brand"><span class="brand-dot"></span>Brightvale Energy</div>
  <nav class="main-nav"><span>Home</span><span>Solutions</span><span>Products</span><span>About Us</span><span>Our Blog</span></nav>
  <a class="btn nav-contact">Contact Us</a>
</header>

<section class="hero">
  <div class="hero-photo" role="img" aria-label="Two engineers in hard hats and hi-vis vests checking plans among rows of rooftop solar panels"></div>
  <h1 class="hero-title">Natural Resources for<br>Electricity to Save Money</h1>
  <a class="btn hero-btn">Learn More</a>
</section>
<div class="badge badge-hero"><span></span></div>

<section class="about">
  <h2 class="about-title">About <span class="accent">Brightvale Energy</span></h2>
  <div class="about-text">
    <p>Brightvale Energy is a national company that specialises in solar solutions for the commercial market. We also provide solutions for the residential market, bringing our uncompromising quality and service to the home.</p>
    <p>The founder of the company has over 10 years experience delivering projects on both a residential and commercial scale, having overseen the installation of more than 3 megawatts of solar projects. They were a pioneer on the first megawatt scale project in Australia.</p>
  </div>
  <a class="btn about-btn">Learn More</a>
  <div class="video">
    <div class="video-photo" role="img" aria-label="Video still of an installer fitting solar panels on a tiled roof under blue sky"></div>
    <svg class="play" viewBox="0 0 72 72"><circle cx="36" cy="36" r="36" fill="#1e1e1e" opacity=".85"/><polygon points="29,22 29,50 52,36" fill="#f05a22"/></svg>
  </div>
</section>

<section class="solutions">
  <h2 class="section-title" style="top:62px">Our <span class="accent">Solution</span></h2>
  <p class="section-lead" style="top:125px">Brightvale Energy is a national company that specialises in solar solutions for the commercial market. We also provide solutions for the residential market, bringing our uncompromising quality and service to the home.</p>
  <div class="solution-card" style="left:120px">
    <div class="solution-photo" role="img" aria-label="Ground-mounted solar array under a blue sky with clouds" style="background:linear-gradient(180deg,#5aa0e0 0%,#b8d4ee 45%,#3a5a8a 70%,#2a3e5e 100%)"></div>
    <div class="solution-label"><h3>For Small Business</h3><span>View More</span></div>
  </div>
  <div class="solution-card" style="left:450px">
    <div class="solution-photo" role="img" aria-label="Technician kneeling beside panels on a commercial roof" style="background:linear-gradient(180deg,#a8b4bc 0%,#7c8a70 40%,#3c4a5e 70%,#2a3444 100%)"></div>
    <div class="solution-label"><h3>For Mid Business</h3><span>View More</span></div>
  </div>
  <div class="solution-card" style="left:780px">
    <div class="solution-photo" role="img" aria-label="Brick family home with solar panels on its roof" style="background:linear-gradient(180deg,#6aa8d8 0%,#9a5a3e 40%,#2e3a4e 60%,#4e7a3e 100%)"></div>
    <div class="solution-label"><h3>For Residential</h3><span>View More</span></div>
  </div>
</section>

<section class="products">
  <h2 class="section-title" style="top:1510px">Our <span class="accent">Products</span></h2>
  <p class="section-lead" style="top:1567px;left:260px;width:680px">when an unknown printer took a galley of type and scrambled it to make a type specimen book. It has survived not only five centuries.</p>

  <div class="product-card" style="left:99px"><div class="product-photo" role="img" aria-label="White single phase inverter unit" style="background:linear-gradient(160deg,#f2f2f2,#d8d8d8)"></div></div>
  <div class="product-card" style="left:356px"><div class="product-photo" role="img" aria-label="Black power optimizer with cables" style="background:linear-gradient(160deg,#ececec,#cfcfcf)"></div></div>
  <div class="product-card" style="left:612px"><div class="product-photo" role="img" aria-label="Tall white three phase inverter unit" style="background:linear-gradient(160deg,#f4f4f4,#dadada)"></div></div>
  <div class="product-card" style="left:869px"><div class="product-photo" role="img" aria-label="Two black solar panels" style="background:linear-gradient(160deg,#2a2e36,#0f1216)"></div></div>

  <div class="product-name" style="left:74px">SunPivot<br>Single Phase Inverters</div>
  <div class="product-name" style="left:331px">SunPivot<br>Power Optimizer</div>
  <div class="product-name" style="left:587px">SunPivot Extended Power<br>Three Phase Inverters</div>
  <div class="product-name" style="left:844px">Morvo Falcon<br>The Budget Workhorse</div>
  <div class="product-price" style="left:74px">$240.00</div>
  <div class="product-price" style="left:331px">$240.00</div>
  <div class="product-price" style="left:587px">$240.00</div>
  <div class="product-price" style="left:844px">$240.00</div>
  <a class="btn all-btn">View All Products</a>
</section>

<section class="reviews">
  <div class="reviews-photo" role="img" aria-label="Solar panels at sunset with warm orange light across a cloudy sky"></div>
</section>
<div class="badge badge-reviews"><span></span></div>
<h2 class="section-title reviews-title">Why They Love Us</h2>
<div class="avatar" role="img" aria-label="Customer portrait" style="left:452px;top:2286px;width:62px;height:62px;background:radial-gradient(circle,#f0905a,#c85a2a)"></div>
<div class="avatar" role="img" aria-label="Portrait of the featured customer" style="left:553px;top:2271px;width:92px;height:92px;background:radial-gradient(circle,#d8b8a0,#7a5a4a)"></div>
<div class="avatar" role="img" aria-label="Customer portrait" style="left:684px;top:2286px;width:62px;height:62px;background:radial-gradient(circle,#f0905a,#c85a2a)"></div>
<p class="review-text">Lorem Ipsum is simply dummy text of the printing and typesetting industry. Lorem Ipsum has been the industry's typesetting industry. Lorem Ipsum has been the industry's standard dummy text ever since the 1500s, when an unknown printer took a galley of type sit amet typesetting gallery.</p>
<div class="review-name">Clara Denholm</div>
<div class="review-role">Small Business Owner</div>
<div class="dots"><i></i><i class="on"></i><i></i></div>

<footer class="site-footer">
  <div class="footer-brand"><span></span>Brightvale Energy</div>
  <div class="footer-col" style="left:406px">
    <h4>Menu</h4>
    <ul><li>Home</li><li>About Us</li><li>Solutions</li><li>Products</li></ul>
  </div>
  <div class="footer-col" style="left:636px">
    <h4>Useful Links</h4>
    <ul><li>Our Blog</li><li>Contact Us</li><li>Terms Of Service</li><li>Privacy Policy</li></ul>
  </div>
  <div class="footer-col" style="left:883px">
    <h4>Get In Touch</h4>
    <ul class="contact-list">
      <li><svg width="16" height="14" viewBox="0 0 16 14"><path d="M2 5a6 6 0 0 1 12 0M5 6a3 3 0 0 1 6 0" fill="none" stroke="#f05a22" stroke-width="1.5"/><rect x="4" y="8" width="8" height="5" rx="1" fill="none" stroke="#f05a22" stroke-width="1.5"/></svg>(123) 456-7890</li>
      <li><svg width="16" height="12" viewBox="0 0 16 12"><rect x="1" y="1" width="14" height="10" fill="none" stroke="#f05a22" stroke-width="1.5"/><path d="M1 1l7 6 7-6" fill="none" stroke="#f05a22" stroke-width="1.5"/></svg>info@brightvaleenergy.com.au</li>
      <li><svg width="16" height="16" viewBox="0 0 16 16"><path d="M8 15s5-5 5-9A5 5 0 0 0 3 6c0 4 5 9 5 9z" fill="none" stroke="#f05a22" stroke-width="1.5"/><circle cx="8" cy="6" r="2" fill="#f05a22"/></svg>00 Main Blvd Melbourne<br>Australia</li>
    </ul>
  </div>
</footer>
<div class="bottom-bar">
  <div class="copyright">Copyright © 2017 Brightvale Energy. All Rights Reserved.</div>
  <div class="social"><i></i><i></i><i></i><i></i></div>
</div>

</body>
</html>
```